Full service meeting planning company needs new business cards

Velmora Linkway is a full service meeting planning company that specializes in on-line conference registration web development and event communications. We combine citywide hotel management, mobile applications, eblast reminders, confirmation letters, and customized reporting to create a seamless registration process. We also manage group motor coach transportation, food and beverages, entertainment, stage and lighting for group of 10 to 4000.

Target Market(s)

Corporations and associations

Industry/Entity Type

Event Planning

Contact Information for Business Card

standard size 3.5" wide and 2" tall

Font styles to use
Serif
Sans Serif

Colors
f37122
f78f20
333333
5c5c5c
9d9d9d
f68d4d

Requirements
Must have
• {name}
• Velmora Linkway
• P.O. Box 7384, Grand Rapids, M I 49568
• www.velmoralinkway.com
• {email}
• {phone}
• {mobile phone}
Nice to have
• Our colors are black, grey and orange as an accent color
Should not have
• I am not happy with our website layout anymore either. It feels dark and old but it does explain who we are pretty well if you'd like to review; www.velmoralinkway.com

```html
<!DOCTYPE html>
<html lang="en">
<head>
<meta charset="utf-8">
<title>Velmora Linkway – Business Card</title>
<link rel="stylesheet" href="https://fonts.googleapis.com/css2?family=Montserrat:wght@600;700&family=Open+Sans:wght@400;600&display=swap">
<style>
  :root {
    --backdrop: #ededed;
    --card-black: #1c1c1c;
    --card-charcoal: #2a2a2a;
    --card-white: #f4f4f4;
    --orange: #f6a81c;
    --orange-deep: #f18a1e;
    --text-light: #e6e6e6;
    --text-dark: #333333;
  }
  * { margin: 0; padding: 0; box-sizing: border-box; }
  html, body { width: 1200px; height: 789px; overflow: hidden; }
  body {
    background: var(--backdrop);
    display: flex;
    align-items: center;
    justify-content: center;
    gap: 50px;
    font-family: "Open Sans", Arial, sans-serif;
  }
  .card {
    width: 525px;
    height: 300px;
    position: relative;
    overflow: hidden;
    box-shadow: 0 6px 18px rgba(0,0,0,0.18);
  }

  /* Front */
  .card-front { background: var(--card-black); display: flex; flex-direction: column; }
  .front-header {
    height: 118px;
    background: var(--card-white);
    padding: 34px 40px 0;
  }
  .company-name {
    font-family: "Montserrat", Arial, sans-serif;
    font-weight: 700;
    font-size: 27px;
    letter-spacing: 0.5px;
    color: var(--text-dark);
    text-transform: uppercase;
  }
  .job-title {
    margin-top: 4px;
    font-family: "Montserrat", Arial, sans-serif;
    font-weight: 600;
    font-size: 12px;
    letter-spacing: 1.5px;
    color: var(--orange-deep);
    text-transform: uppercase;
  }
  .accent-stripe {
    height: 12px;
    background: linear-gradient(90deg, var(--orange), var(--orange-deep));
  }
  .front-contacts {
    flex: 1;
    background: linear-gradient(180deg, var(--card-charcoal), var(--card-black));
    display: grid;
    grid-template-columns: 1fr 1fr;
    align-content: center;
    row-gap: 26px;
    padding: 0 40px;
  }
  .contact-item { display: flex; align-items: center; gap: 12px; }
  .contact-icon { width: 24px; height: 24px; flex: none; }
  .contact-text {
    font-size: 10px;
    line-height: 1.45;
    color: var(--text-light);
    letter-spacing: 0.3px;
  }

  /* Back */
  .card-back { display: flex; flex-direction: column; background: var(--card-black); }
  .band-black-top { height: 92px; background: var(--card-black); }
  .band-orange {
    height: 104px;
    background: linear-gradient(90deg, var(--orange), var(--orange-deep));
    display: flex;
    align-items: center;
    justify-content: center;
    gap: 14px;
  }
  .brand-mark {
    width: 34px; height: 34px;
    border-radius: 50%;
    background: var(--card-white);
  }
  .brand-name {
    font-family: "Montserrat", Arial, sans-serif;
    font-weight: 700;
    font-size: 20px;
    letter-spacing: 1px;
    color: var(--card-white);
    text-transform: uppercase;
  }
  .band-white { height: 18px; background: var(--card-white); }
  .band-black-bottom { flex: 1; background: var(--card-black); }
</style>
</head>
<body>

  <section class="card card-front" aria-label="Business card front">
    <header class="front-header">
      <h1 class="company-name">Velmora Linkway</h1>
      <p class="job-title">Graphic Designer</p>
    </header>
    <div class="accent-stripe"></div>
    <div class="front-contacts">
      <div class="contact-item">
        <svg class="contact-icon" viewBox="0 0 24 24" aria-hidden="true">
          <circle cx="12" cy="12" r="12" fill="#f6a81c"/>
          <rect x="6.5" y="8" width="11" height="8" rx="1" fill="none" stroke="#1c1c1c" stroke-width="1.4"/>
          <path d="M6.8 8.4 L12 12.6 L17.2 8.4" fill="none" stroke="#1c1c1c" stroke-width="1.4"/>
        </svg>
        <p class="contact-text">info@velmoralinkway.com</p>
      </div>
      <div class="contact-item">
        <svg class="contact-icon" viewBox="0 0 24 24" aria-hidden="true">
          <circle cx="12" cy="12" r="12" fill="#f6a81c"/>
          <path d="M7 13.5 L12 8.5 L17 13.5 M8.5 12.5 V17 H15.5 V12.5" fill="none" stroke="#1c1c1c" stroke-width="1.6" stroke-linejoin="round"/>
        </svg>
        <p class="contact-text">P.O. Box 7384, Grand Rapids,<br>M I 49568</p>
      </div>
      <div class="contact-item">
        <svg class="contact-icon" viewBox="0 0 24 24" aria-hidden="true">
          <circle cx="12" cy="12" r="12" fill="#f6a81c"/>
          <path d="M8.6 6.8 L10.4 6.5 L11.4 9.3 L10 10.4 C10.7 12 11.9 13.2 13.5 13.9 L14.6 12.6 L17.3 13.6 L17 15.4 C16.8 16.3 15.9 16.8 15 16.6 C11.3 15.8 8.1 12.6 7.3 8.9 C7.1 8 7.7 7 8.6 6.8 Z" fill="#1c1c1c"/>
        </svg>
        <p class="contact-text">+1 616 555 0142<br>+1 616 555 0187</p>
      </div>
      <div class="contact-item">
        <svg class="contact-icon" viewBox="0 0 24 24" aria-hidden="true">
          <circle cx="12" cy="12" r="12" fill="#f6a81c"/>
          <circle cx="12" cy="12" r="5.5" fill="none" stroke="#1c1c1c" stroke-width="1.4"/>
          <path d="M6.5 12 H17.5 M12 6.5 C9.8 9 9.8 15 12 17.5 M12 6.5 C14.2 9 14.2 15 12 17.5" fill="none" stroke="#1c1c1c" stroke-width="1.1"/>
        </svg>
        <p class="contact-text">www.velmoralinkway.com</p>
      </div>
    </div>
  </section>

  <section class="card card-back" aria-label="Business card back">
    <div class="band-black-top"></div>
    <div class="band-orange">
      <span class="brand-mark" aria-hidden="true"></span>
      <span class="brand-name">Velmora Linkway</span>
    </div>
    <div class="band-white"></div>
    <div class="band-black-bottom"></div>
  </section>

</body>
</html>
```